Kelvanta (www.kelvanta.net) needs exciting professional PowerPoint pitch template

Kelvanta is an exciting new start-up targeting innovative ways to engage with retail customers at the point of sale.

Our customers are looking for us to help them increase the "wallet share" of their retail customers. The retail customer has their wallet open at the Point of Sale and are paying money to our customer. At Kelvanta we are all about attracting the attention of the retail customer AT THAT POINT IN TIME and engaging the retail customer in spending a little more in that store or another store that has a relationship to the retail customer's purchase.

Our customers are the owners of very large supermarkets, chain stores, and financial institutions, and therefore when we pitch a proposal to these buyers it needs to be slick, professional, and very memorable.

The PowerPoint sales presentation template is a key part of striking that impression.

Here is some background...

Our Vision
Through applying new thinking to a mature industry we are reinventing selected segments of the Australian retail messaging business, generating significant value for our customers, our suppliers, and our owners.
We operate with integrity, agility, and intelligence to doing things smarter, faster and more efficiently.
We bring deep industry expertise, deep relationships with customers and suppliers, and a will to see the old ways give way to smarter ways – this is why we win.
From this economically sustainable platform, we will examine the disruption of other market segments by further leveraging the elements that make us successful.

Our Values
With our clients, with our suppliers, with our staff, and with our owners:
# We Partner – We align the interest of all stakeholders by striving to ensure everything we do is mutually beneficial and commercially sustainable in the long term. We are clear with all our stakeholders about what our expectations are of them, and we seek clarity from them in their expectations of us.
# We Innovate – In the segments we choose to compete in, we bring fresh ideas, new business processes, the right relationships, and the right technology to ensure the supply chain is nimble, competitive, and reliable.
# We are Accountable – We say what we will do, and then do what we say.
# We Perform – We use our skills, relationships, and reputation to deliver value to our customers, suppliers, and owners.

Initially we are building our business from low-tech through printing promotional offers and retailer messages on ATM and EFTPOS receipts, but as soon as cash flow supports it we will be engaging in high-tech real-time targeted offers to the specific consumer through video wall offers as people are at the checkout or walking through the shopping centre.

I'd like the PowerPoint template to reflect our vision and values.

The PowerPoint template will be used in communicating our proposals to our clients, and needs to catch and hold our audiences attention.

Please check out the web site we have just launched - it is pretty basic but it has only been up a week. We intend to sharpen it over the coming weeks, but you'll get the idea of what our core messages are.

I have recently sourced a logo from ArtHarbor, plus business cards, and have attached the source files for your reference.
Updates

Hi everybody.  Thanks for the designs submitted so far.  Your submissions have helped me understand what I do and don't prefer, and I have updated the "Must Have/Nice to Have/Shouldn't Have" criteria accordingly.  I have also uploaded a powerpoint template that I had at a company I udsed to run that has the sort of visual theme I find appealing. I have more time to provide feedback now that the week is over, so I will comment on individual designs shortly, and I will respond to queries directed to me.

Kind Regards - Grant

Target Market(s)

Our customers are large corporations that have professional Point Of Sale marketing experts looking for a supplier with an edge over others in a crowded market. The buyer of our product and services is ultimately a communications expert. They want to see distinctive competence, and an agility of thinking that will make them money through driving more consumer spending.

Industry/Entity Type

Financial

Font styles to use
Sans Serif

Colors
34a7d7
0892cd
3276b5

Requirements
Must have
• The following Slides: Title Slide, Agenda, About Kelvanta, Thank you
The pages must be easy on the eye.
The final product must be a PowerPoint template file with the usual "Title", "Title and Content", "Title & Table", and "Blank" page types.
Widescreen format please.
Nice to have
• The pages should have an eye-catching visual element running through all the pages. I have attached a template from a company i used to be involved with that has a visual theme running through it that I like.
Plenty of whitespace - have a look at www.kelvanta.net.
Bonus points for pulling the text from the brief into the template.
Use "Innovation - Integrity - Service" as the tag line.
Should not have
• Pages should not be busy.
Stay away from too much black. I know the cards have black, but the presentation shouldn't.
I dont like serifed fonts. Use Dravelle's Modern UI style for insporation.
The "Bringing Lumora" tag line was an invention of the logo designer that we do not want to cary forward. Please do not use it.

```html
<!DOCTYPE html>
<html lang="en">
<head>
<meta charset="UTF-8">
<title>Kelvanta – Title and Content</title>
<link rel="stylesheet" href="https://fonts.googleapis.com/css2?family=PT+Sans:wght@400;700&display=swap">
<style>
  :root {
    --brand-blue: #0a78c2;
    --ink: #3a3a3a;
    --muted: #6d6e71;
    --night: #231f20;
    --paper: #ffffff;
  }
  * { margin: 0; padding: 0; box-sizing: border-box; }
  html, body { width: 1200px; height: 900px; overflow: hidden; background: var(--paper); }
  .slide {
    position: relative;
    width: 1200px;
    height: 900px;
    overflow: hidden;
    background: var(--paper);
    font-family: "PT Sans", Tahoma, sans-serif;
  }
  .title-band {
    position: absolute;
    left: 0; top: 0;
    width: 1200px; height: 93px;
    background: var(--brand-blue);
  }
  .slide-title {
    position: absolute;
    left: 30px; top: 15px;
    color: var(--paper);
    font-size: 48px;
    font-weight: 700;
    line-height: 1.1;
    letter-spacing: 1.6px;
  }
  .brand-tab {
    position: absolute;
    left: 845px; top: 27px;
    width: 348px; height: 66px;
    background: var(--paper);
    border-radius: 10px 10px 0 0;
    display: flex;
    align-items: center;
    justify-content: center;
  }
  .brand-name {
    color: var(--muted);
    font-size: 34px;
    font-weight: 400;
    line-height: 1;
  }
  .point-list {
    position: absolute;
    left: 0; top: 0;
    list-style: none;
  }
  .point {
    position: absolute;
    left: 93px;
    width: 1060px;
    color: var(--ink);
    font-size: 23px;
    letter-spacing: 0.9px;
    line-height: 37.5px;
    white-space: nowrap;
  }
  .point::before {
    content: "";
    position: absolute;
    left: -58px; top: 2px;
    width: 0; height: 0;
    border-top: 17px solid transparent;
    border-bottom: 17px solid transparent;
    border-left: 22px solid var(--brand-blue);
  }
  .point-1 { top: 202px; }
  .point-2 { top: 295px; }
  .point-3 { top: 425px; }
  .point-4 { top: 593px; }
  .footer-wave {
    position: absolute;
    left: 0; top: 0;
    width: 1200px; height: 900px;
  }
  .footer-note {
    position: absolute;
    left: 30px; top: 849px;
    color: var(--paper);
    font-size: 20px;
    letter-spacing: 0.8px;
  }
  .page-number {
    position: absolute;
    left: 1095px; top: 825px;
    width: 60px; height: 60px;
    border-radius: 50%;
    background: var(--brand-blue);
    border: 2px solid #4aa3de;
    color: var(--paper);
    font-size: 22px;
    font-weight: 700;
    display: flex;
    align-items: center;
    justify-content: center;
  }
</style>
</head>
<body>
<main class="slide">
  <header class="title-band">
    <h1 class="slide-title">Project Title here</h1>
    <div class="brand-tab">
      <span class="brand-name">Kelvanta</span>
    </div>
  </header>

  <ul class="point-list">
    <li class="point point-1">Lorem ipsum dolor sit ipsum Lorem ipsum dolor sit ipsum Lorem ipsum dolor sit ipsum</li>
    <li class="point point-2">Lorem ipsum dolor sit ipsum Lorem ipsum dolor sit ipsum Lorem ipsum dolor sit ipsumLorem<br>ipsum dolor sit ipsum Lorem ipsum dolor</li>
    <li class="point point-3">Lorem Lorem ipsum dolor sit ipsum Lorem ipsum dolor sit ipsum Lorem ipsum dolor sit ipsum<br>Lorem ipsum dolor sit ipsum Lorem ipsum dolor sit ipsum Lorem ipsum dolor sit ipsumipsum<br>dolor sit ipsum Lorem ipsum dolor sit ipsum Lorem ipsum dolor sit ipsum</li>
    <li class="point point-4">Lorem ipsum dolor sit ipsum Lorem ipsum dolor sit ipsum Lorem ipsum dolor sit ipsumLorem<br>ipsum dolor sit ipsum Lorem ipsum dolor</li>
  </ul>

  <svg class="footer-wave" viewBox="0 0 1200 900" aria-hidden="true">
    <path d="M0,756 C420,893 900,903 1200,746 L1200,900 L0,900 Z" fill="var(--night)"/>
    <path d="M0,748 C420,885 900,895 1200,738" fill="none" stroke="var(--brand-blue)" stroke-width="4"/>
  </svg>

  <footer>
    <p class="footer-note">All Rights Reserved kelvanta</p>
    <div class="page-number">01</div>
  </footer>
</main>
</body>
</html>
```